Lorna Vee Tresses Fancy Business Card’s

I want my business cards to be elite, original and very classy. I want the business cards to match the colors of my logo and to match the design posted. I would love the design of the picture I posted

I want the card all white .
The dripping on the top of the card I want it to match the pink color in my logo that’s also posted .
I need my logo on the business card !
I need my Instagram- @lorna.vee.tresses__
And my phone number - 555 207 9362

Target Market(s)

My target market is young woman age 23 to older woman to the age of 65
I want both older and younger women to love my design . I don’t want any cheap looking business cards

Industry/Entity Type

Hair And Beauty

Contact Information for Business Card

Add my logo
Add my Instagram- @lorna.vee.tresses__
My number - 555 207 9362
My website- www.lornaveetresses-example.com

Font styles to use
Serif
Script

Colors
ffffff
e667a6
e34298

Requirements
Must have
• The business cards must have my logo, my number , my website, and my Instagram!
Nice to have
• Nice to have glitter words that match my logo
• The business cards must look classy and mature
• I want them to be very unique!!
Should not have
• Should not have any colors that doesn’t match my logo ! This is very important! Please

```html
<!DOCTYPE html>
<html lang="en">
<head>
<meta charset="utf-8">
<title>Lorna Vee Tresses – Business Card</title>
<link rel="stylesheet" href="https://fonts.googleapis.com/css2?family=Lato:wght@400;700&display=swap">
<style>
  :root {
    --pink: #e34298;
    --pink-soft: #e667a6;
    --white: #ffffff;
    --grey-arc: #7a7a76;
    --backdrop: #dcdcdc;
  }
  * { margin: 0; padding: 0; box-sizing: border-box; }
  html, body {
    width: 1200px; height: 802px; overflow: hidden;
    background: var(--backdrop);
    font-family: "Lato", sans-serif;
  }
  .stage { position: relative; width: 1200px; height: 802px; }
  .card {
    position: absolute; top: 269px;
    width: 442px; height: 264px;
    overflow: hidden;
  }
  .card--front { left: 134px; background: var(--white); }
  .card--back  { left: 624px; background: var(--pink); }

  .card__shape { position: absolute; inset: 0; }

  .contact {
    position: absolute; left: 16px; top: 101px;
    list-style: none; color: var(--white);
    font-size: 12px; line-height: 1;
    white-space: nowrap;
  }
  .contact__item {
    display: flex; align-items: center; gap: 5px;
    height: 16px; margin-bottom: 6px;
  }
  .contact__item--social { margin-top: 17px; }
  .contact__icon { width: 15px; height: 15px; flex: none; }

  .wordmark {
    position: absolute; text-align: center;
    font-family: "Lato", sans-serif; font-weight: 700;
    line-height: 1.05;
  }
  .wordmark--front {
    left: 250px; width: 180px; top: 150px;
    color: var(--pink); font-size: 26px;
  }
  .wordmark--back {
    left: 0; width: 100%; top: 96px;
    color: var(--white); font-size: 36px;
  }
</style>
</head>
<body>
<main class="stage">

  <section class="card card--front" aria-label="Business card, contact side">
    <svg class="card__shape" viewBox="0 0 442 264" width="442" height="264" aria-hidden="true">
      <path d="M169 0 Q 324 132 169 264" fill="none" stroke="var(--grey-arc)" stroke-width="6"/>
      <path d="M0 0 H163 Q 310 132 163 264 H0 Z" fill="var(--pink)" stroke="var(--white)" stroke-width="2"/>
    </svg>

    <ul class="contact">
      <li class="contact__item">
        <svg class="contact__icon" viewBox="0 0 16 16" aria-hidden="true">
          <circle cx="8" cy="8" r="7" fill="none" stroke="var(--white)" stroke-width="1.3"/>
          <path d="M5.4 4.3l1.3 0 .6 1.8-.9.7c.4 1 1.1 1.7 2 2.1l.7-.9 1.8.6v1.3c0 .5-.4.8-.9.8C7.1 10.5 5.5 8.9 4.6 5.2c0-.5.3-.9.8-.9z" fill="var(--white)"/>
        </svg>
        <span>555 207 9362</span>
      </li>
      <li class="contact__item">
        <svg class="contact__icon" viewBox="0 0 16 16" aria-hidden="true">
          <g fill="none" stroke="var(--white)" stroke-width="1.2">
            <circle cx="8" cy="8" r="7"/>
            <ellipse cx="8" cy="8" rx="3" ry="7"/>
            <path d="M1 8h14M2 4.5h12M2 11.5h12"/>
          </g>
        </svg>
        <span>www.lornaveetresses-example.com</span>
      </li>
      <li class="contact__item contact__item--social">
        <svg class="contact__icon" viewBox="0 0 16 16" aria-hidden="true">
          <circle cx="8" cy="8" r="7" fill="none" stroke="var(--white)" stroke-width="1.3"/>
        </svg>
        <span>@lorna.vee.tresses__</span>
      </li>
    </ul>

    <p class="wordmark wordmark--front">Lorna Vee<br>Tresses</p>
  </section>

  <section class="card card--back" aria-label="Business card, name side">
    <p class="wordmark wordmark--back">Lorna Vee<br>Tresses</p>
  </section>

</main>
</body>
</html>
```